Brimlow Oakville Cabernet Sauvignon-Wine label design

We need a package design for an up market wine brand named, Brimlow. It will be a Cabernet Sauvignon from the Oakville AVA of Napa Valley. We are looking for a stylish modern label that will stand out on a retail shelf. We want the label to be attention grabbing and stylish while presenting an up market luxury brand.
Updates

Sick

Requirements
Must have
• Must have the words(in order of importance)
-Brimlow
-Cabernet Sauvignon
-Oakville
-Napa Valley
-2018

Must be designed for a traditional "Bordeaux" style bottle (Bottle specs in uploaded files)
Should not have
• Any images of grapes, vineyards, wine glasses or bottles

```html
<!DOCTYPE html>
<html lang="en">
<head>
<meta charset="utf-8">
<title>Brimlow 2018 Cabernet Sauvignon Label</title>
<link rel="stylesheet" href="https://fonts.googleapis.com/css2?family=Bodoni+Moda:opsz,wght@6..96,400;6..96,500&display=swap">
<style>
  :root {
    --label-black: #000000;
    --ink-white: #ffffff;
    --mark-glow: #e8e8e8;
    --mark-mid: #6a6a6a;
  }
  html, body {
    margin: 0;
    padding: 0;
    width: 1200px;
    height: 2530px;
    overflow: hidden;
    background: var(--label-black);
  }
  .label {
    position: relative;
    width: 1200px;
    height: 2530px;
    overflow: hidden;
    background: var(--label-black);
    color: var(--ink-white);
    font-family: "Bodoni Moda", "Didot", serif;
    font-variation-settings: "opsz" 96;
  }
  .brand-name {
    position: absolute;
    top: 340px;
    left: 0;
    width: 100%;
    margin: 0;
    text-align: center;
    white-space: nowrap;
    font-size: 240px;
    font-weight: 400;
    line-height: 1;
    letter-spacing: -4px;
    text-transform: lowercase;
  }
  .emblem {
    position: absolute;
    left: 140px;
    top: 712px;
    width: 920px;
    height: 920px;
  }
  .wine-details {
    position: absolute;
    top: 1770px;
    left: 0;
    width: 100%;
    text-align: center;
    margin: 0;
  }
  .vintage {
    display: block;
    font-size: 68px;
    line-height: 1.2;
  }
  .varietal {
    display: block;
    margin-top: 4px;
    font-size: 72px;
    line-height: 1.2;
    letter-spacing: 1px;
    white-space: nowrap;
  }
  .appellation {
    position: absolute;
    top: 2180px;
    left: 0;
    width: 100%;
    text-align: center;
    margin: 0;
    font-size: 60px;
    line-height: 1.62;
    letter-spacing: 1px;
  }
  .appellation span { display: block; }
</style>
</head>
<body>
  <main class="label">
    <h1 class="brand-name">Brimlow</h1>

    <svg class="emblem" viewBox="0 0 920 920" role="img" aria-label="Spiral of white dots radiating outward from a central point">
      <defs>
        <radialGradient id="emblem-tone" cx="50%" cy="50%" r="50%">
          <stop offset="0%" stop-color="var(--mark-mid)" stop-opacity="0.35"/>
          <stop offset="60%" stop-color="var(--mark-mid)" stop-opacity="0.55"/>
          <stop offset="92%" stop-color="var(--mark-glow)" stop-opacity="0.75"/>
          <stop offset="100%" stop-color="var(--mark-glow)" stop-opacity="0"/>
        </radialGradient>
      </defs>
      <circle cx="460" cy="460" r="460" fill="url(#emblem-tone)"/>
    </svg>

    <p class="wine-details">
      <span class="vintage">2018</span>
      <span class="varietal">CABERNET SAUVIGNON</span>
    </p>

    <p class="appellation">
      <span>OAKVILLE</span>
      <span>NAPA VALLEY</span>
    </p>
  </main>
</body>
</html>
```